Fresh Idea for Winter Car Combo Box Cover

We are a business that manufactures and distributes icemelt for roads and sidewalks. We are introducing a new car combo set to help you Get Back On Track when you car is snowed in. This is our current box cover. We are looking for an eye catching new look. The measurements of the rectangular box are 25H x 9W.
Logo was uploaded only to show colors, this is not the clearest picture so only use for color reference please!
Updates

Project Deadline Extended
Reason: To give time to designers who have submitted designs time to perfect their ideas and to give new designers a chance to submit their ideas.

Target Market(s)

Big Box Stores such as Valmark, TKs, Crate Yard etc

Industry/Entity Type

Business

Colors
0455a3
3276b5
85acd3

Requirements
Must have
• Must have the three items on the picture provided

```html
<!DOCTYPE html>
<html lang="en">
<head>
<meta charset="utf-8">
<title>Kestrel Seasonal Products – Get Back On Track Box Cover</title>
<link rel="stylesheet" href="https://fonts.googleapis.com/css2?family=Montserrat:wght@500;600;700;800&family=Open+Sans:wght@400;600&display=swap">
<style>
  :root {
    --brand-deep: #0455a3;
    --brand-mid: #3276b5;
    --brand-light: #85acd3;
    --ice: #dce8f4;
    --panel-white: #f7f9fc;
    --ink: #1d2f5c;
    --page: #ffffff;
  }
  * { box-sizing: border-box; margin: 0; padding: 0; }
  html, body {
    width: 1200px; height: 900px; overflow: hidden;
    background: var(--page);
    font-family: "Open Sans", sans-serif;
  }
  .canvas {
    position: relative; width: 1200px; height: 900px;
    display: flex; justify-content: center; align-items: center;
  }
  .box-dieline { display: flex; height: 833px; box-shadow: 0 6px 24px rgba(4,85,163,.15); }

  /* Side spine */
  .box-spine {
    position: relative; width: 86px; height: 100%;
    background: linear-gradient(90deg, var(--brand-deep), var(--brand-mid));
    display: flex; align-items: center; justify-content: center;
  }
  .spine-brand {
    writing-mode: vertical-rl;
    display: flex; align-items: center; gap: 8px;
    color: #ffffff; font-family: "Montserrat", sans-serif; font-weight: 700;
    font-size: 20px; letter-spacing: .5px; white-space: nowrap;
  }
  .spine-brand .brand-dot { width: 12px; height: 12px; border-radius: 50%; background: #ffffff; }

  /* Front panel */
  .box-front {
    position: relative; width: 300px; height: 100%;
    background: linear-gradient(180deg, var(--panel-white), #eef3f9 60%, var(--panel-white));
    overflow: hidden;
  }
  .wave { position: absolute; left: 0; width: 100%; display: block; }
  .wave-top { top: 0; height: 110px; }
  .wave-bottom { bottom: 0; height: 140px; }

  .front-brand {
    position: absolute; top: 108px; left: 0; width: 100%;
    display: flex; align-items: center; justify-content: center; gap: 10px;
  }
  .front-brand .brand-dot { width: 34px; height: 34px; border-radius: 50%; background: var(--brand-light); }
  .brand-name {
    color: var(--ink); font-family: "Montserrat", sans-serif; font-weight: 700;
    line-height: 1.05;
  }
  .brand-name .brand-word { display: block; font-size: 30px; letter-spacing: .5px; }
  .brand-name .brand-sub { display: block; font-size: 12px; letter-spacing: .2px; }

  .headline-banner {
    position: absolute; top: 176px; left: 20px; width: 252px; height: 46px;
    background: linear-gradient(90deg, var(--brand-deep), var(--brand-mid));
    color: #ffffff; font-family: "Montserrat", sans-serif; font-weight: 800;
    font-size: 18px; letter-spacing: .5px;
    display: flex; align-items: center; justify-content: center;
    box-shadow: 0 3px 6px rgba(4,85,163,.3);
  }

  .product-tile {
    position: absolute; border: 2px solid var(--brand-deep); border-radius: 10px;
    background: #ffffff; overflow: hidden;
  }
  .product-tile .fill { width: 100%; height: 100%; }
  .tile-shovel { top: 236px; left: 22px; width: 150px; height: 82px; }
  .tile-shovel .fill { background: linear-gradient(135deg, #ffffff 20%, #5aa7de 60%, #ffffff 95%); }
  .tile-tire { top: 298px; left: 128px; width: 148px; height: 82px; }
  .tile-tire .fill { background: linear-gradient(160deg, #7a2a2a 0%, #5c5f66 30%, #d8dde3 65%, #f0f2f5 100%); }
  .tile-cleats { top: 362px; left: 22px; width: 190px; height: 84px; }
  .tile-cleats .fill { background: linear-gradient(135deg, #ffffff 10%, #2c2f36 45%, #1a1c20 65%, #ffffff 95%); }

  .decor-frost {
    position: absolute; border-radius: 50%;
    background: radial-gradient(circle, rgba(133,172,211,.35), rgba(133,172,211,0) 70%);
  }
  .frost-left { top: 430px; left: -30px; width: 120px; height: 120px; }
  .frost-right { top: 560px; right: -40px; width: 170px; height: 170px; }

  .feature-copy {
    position: absolute; top: 458px; left: 0; width: 100%;
    text-align: center; color: var(--ink);
  }
  .feature-title {
    font-family: "Montserrat", sans-serif; font-weight: 700;
    font-size: 13px; color: var(--brand-deep); margin-top: 8px;
  }
  .feature-title:first-child { margin-top: 0; }
  .feature-list { list-style: none; font-size: 8.5px; line-height: 1.4; margin-top: 2px; }
  .feature-note { font-size: 8px; letter-spacing: .4px; text-transform: uppercase; margin-top: 3px; }
  .steps { list-style: none; font-size: 8.5px; line-height: 1.55; margin-top: 3px; }
  .steps .num {
    display: inline-flex; width: 10px; height: 10px; border-radius: 50%;
    background: var(--brand-deep); color: #fff; font-size: 7px; font-weight: 600;
    align-items: center; justify-content: center; margin-right: 3px; vertical-align: 1px;
  }
  .feature-body { font-size: 8.5px; line-height: 1.4; margin-top: 3px; }
</style>
</head>
<body>
<main class="canvas">
  <div class="box-dieline">
    <aside class="box-spine">
      <div class="spine-brand"><span class="brand-dot"></span>KESTREL SEASONAL PRODUCTS, INC.</div>
    </aside>

    <section class="box-front">
      <svg class="wave wave-top" viewBox="0 0 300 110" preserveAspectRatio="none" aria-hidden="true">
        <path d="M0 0 H300 V62 C240 40 170 92 90 70 C50 60 20 62 0 70 Z" fill="var(--brand-deep)"/>
        <path d="M0 0 H300 V40 C250 26 190 58 120 46 C70 38 30 40 0 48 Z" fill="var(--brand-mid)"/>
        <path d="M0 0 H300 V16 C260 22 270 30 250 22 C230 30 220 14 190 20 C170 30 160 16 140 22 C120 32 110 14 80 20 C60 30 50 16 30 20 C15 28 8 18 0 20 Z" fill="#ffffff"/>
        <path d="M0 80 C40 70 80 74 120 84 C190 100 250 66 300 74" fill="none" stroke="var(--brand-light)" stroke-width="3"/>
        <path d="M0 88 C50 80 90 86 130 94 C200 106 260 80 300 84" fill="none" stroke="var(--ice)" stroke-width="2"/>
      </svg>

      <div class="front-brand">
        <span class="brand-dot"></span>
        <div class="brand-name">
          <span class="brand-word">KESTREL</span>
          <span class="brand-sub">SEASONAL PRODUCTS, INC.</span>
        </div>
      </div>

      <div class="headline-banner">GET BACK ON TRACK</div>

      <div class="product-tile tile-shovel"><div class="fill" role="img" aria-label="Photo of the blue compact shovel in three snap pieces: scoop, metal shaft and D-grip handle"></div></div>
      <div class="product-tile tile-tire"><div class="fill" role="img" aria-label="Photo of a car tire on a traction tool in packed snow"></div></div>
      <div class="product-tile tile-cleats"><div class="fill" role="img" aria-label="Photo of a pair of black snow shoe cleats"></div></div>

      <div class="decor-frost frost-left" aria-hidden="true"></div>
      <div class="decor-frost frost-right" aria-hidden="true"></div>

      <div class="feature-copy">
        <h2 class="feature-title">Traction Tool For Your Car</h2>
        <ul class="feature-list">
          <li>• Eliminates shoveling and pushing</li>
          <li>• Easy to use, easy to store</li>
          <li>• Durable, strong construction</li>
        </ul>
        <h2 class="feature-title">Compact Shovel</h2>
        <p class="feature-note">3 Easy Snap Pieces For The Car</p>
        <ol class="steps">
          <li><span class="num">1</span>D-Grip Handle for a Comfortable Grip</li>
          <li><span class="num">2</span>Sturdy Metal Shaft with snap-lock connectors</li>
          <li><span class="num">3</span>Lightweight scoop designed for easy use</li>
        </ol>
        <h2 class="feature-title">Snow Shoe Cleats</h2>
        <p class="feature-body">Full-foot slip protection over shoes,<br>boots and athletic shoes</p>
      </div>

      <svg class="wave wave-bottom" viewBox="0 0 300 140" preserveAspectRatio="none" aria-hidden="true">
        <path d="M0 40 C60 20 120 60 190 44 C240 32 270 30 300 36" fill="none" stroke="var(--brand-light)" stroke-width="3"/>
        <path d="M0 48 C60 30 120 70 190 54 C240 42 270 40 300 46 V140 H0 Z" fill="var(--brand-mid)"/>
        <path d="M0 66 C70 50 130 90 200 74 C250 62 280 62 300 66 V140 H0 Z" fill="var(--brand-deep)"/>
        <path d="M0 140 V122 C10 130 20 112 40 120 C60 132 70 112 100 118 C120 130 140 110 170 118 C190 128 210 112 240 118 C260 128 280 112 300 118 V140 Z" fill="#ffffff"/>
      </svg>
    </section>
  </div>
</main>
</body>
</html>
```